Popup-Fenster Design für Öffnungszeiten
Zielgruppe
Planung und Realisierung von individuellen Kaminen.
Aufgabenstellung
Für unsere Website www.lindenhaus-torvel.de benötigen wir ein Popup-Fenster für die Startseite. Da das Geschäft nicht jeden Tag und zu festen Zeit geöffnet hat, soll der Kunde direkt sehen können, wann das Geschäft das nächste Mal geöffnet hat. Das Popup-Fenster soll auffällig, jedoch nicht überladen und aufdringlich sein. Einen eigenen Entwurf (der mir nicht gefällt) habe ich hochgeladen. Vielleicht benötigt dieser nur noch einen Feinschliff!? Es muss nicht reckteckig sein, ich bin auch für runde oder ovale Formen offen. Der dort eingesetzte Text sollte als Platzhalter eingesetzt werden. Bei Fragen können Sie mir gerne eine Nachricht zukommen lassen.

```html
<!DOCTYPE html>
<html lang="de">
<head>
<meta charset="utf-8">
<title>Lindenhaus – Öffnungszeiten</title>
<link rel="stylesheet" href="https://fonts.googleapis.com/css2?family=Raleway:wght@300;400&family=Playfair+Display:ital,wght@1,900&family=Barlow+Semi+Condensed:wght@400;500&family=Open+Sans:wght@400&display=swap">
<style>
  :root {
    --sidebar: #1b1b1b;
    --nav-text: #8b8b86;
    --gold: #c7ad62;
    --gold-light: #dcc47c;
    --gold-dark: #b89a4c;
    --white: #ffffff;
    --popup-top: #3d3e41;
    --popup-bottom: #050505;
    --divider: #6a6a6a;
    --muted: #d8d8d8;
  }
  * { box-sizing: border-box; margin: 0; padding: 0; }
  html, body { width: 1200px; height: 577px; overflow: hidden; background: var(--sidebar); }
  .page { position: relative; width: 1200px; height: 577px; overflow: hidden; }

  .sidebar { position: absolute; left: 0; top: 0; width: 264px; height: 577px; background: var(--sidebar); }
  .brand-name { position: absolute; left: 0; width: 264px; top: 112px; text-align: center;
    font-family: "Raleway", sans-serif; font-weight: 400; font-size: 18px; color: var(--gold); }
  .main-nav { position: absolute; left: 44px; top: 223px; list-style: none; }
  .main-nav li { font-family: "Raleway", sans-serif; font-weight: 400; font-size: 16px; color: var(--nav-text); height: 45.7px; }
  .legal { position: absolute; left: 44px; top: 539px; font-family: "Raleway", sans-serif; font-size: 10.5px; color: var(--nav-text); }

  .hero { position: absolute; left: 264px; top: 0; width: 936px; height: 577px;
    background:
      linear-gradient(180deg, #b9a78e 0%, #c7b59a 8%, transparent 12%),
      linear-gradient(180deg, #aeb7c2 0%, #dfe3e8 25%, #c9ccce 33%, #7b7469 42%, #5f574c 58%, #9c968d 72%, #6b655e 84%, #8a7764 100%); }
  .hero-title { position: absolute; left: 264px; width: 936px; top: 215px; text-align: center;
    font-family: "Raleway", sans-serif; font-weight: 300; font-size: 56px; color: var(--white); letter-spacing: 0.5px; }
  .hero-tagline { position: absolute; left: 264px; width: 936px; top: 283px; text-align: center;
    font-family: "Playfair Display", serif; font-style: italic; font-weight: 900; font-size: 34px; color: var(--white); }
  .hero-cta { position: absolute; left: 619px; top: 509px; font-family: "Raleway", sans-serif; font-size: 11px;
    letter-spacing: 1.6px; color: #e4e4e4; }
  .hero-chevron { position: absolute; left: 725px; top: 535px; }

  .hours-popup { position: absolute; left: 823px; top: 351px; width: 345px; height: 192px; border-radius: 4px;
    background: linear-gradient(180deg, var(--popup-top) 0%, #1d1e20 60%, var(--popup-bottom) 100%);
    font-family: "Open Sans", sans-serif; color: var(--white); text-align: center; }
  .hours-close { position: absolute; left: 1156px; top: 340px; width: 22px; height: 22px; border-radius: 50%;
    background: var(--white); color: #111; font-family: "Barlow Semi Condensed", sans-serif; font-weight: 500;
    font-size: 15px; line-height: 21px; text-align: center; }
  .hours-title { position: absolute; left: 0; top: 19px; width: 345px; height: 35px;
    background: linear-gradient(180deg, var(--gold-light), var(--gold) 55%, var(--gold-dark));
    font-family: "Barlow Semi Condensed", sans-serif; font-weight: 500; font-size: 21px; letter-spacing: 0.6px;
    line-height: 35px; color: #141414; }
  .hours-intro { position: absolute; left: 0; width: 345px; top: 67px; font-size: 14.5px; }
  .hours-list { position: absolute; left: 92px; top: 91px; font-size: 12.3px; line-height: 16.5px; text-align: left; white-space: nowrap; }
  .hours-list span { display: inline-block; width: 62px; }
  .hours-divider { position: absolute; left: 34px; top: 136px; width: 279px; height: 1px; background: var(--divider); }
  .hours-links { position: absolute; left: 0; width: 345px; top: 143px; font-size: 12.5px; line-height: 17px; color: var(--muted); }
</style>
</head>
<body>
<div class="page">
  <aside class="sidebar">
    <p class="brand-name">Lindenhaus</p>
    <ul class="main-nav">
      <li>ÜBER UNS</li>
      <li>KAMINÖFEN</li>
      <li>HOLZKAMINE</li>
      <li>GASKAMINE</li>
      <li>AUSSTELLUNG</li>
      <li>KONTAKT</li>
    </ul>
    <p class="legal">Impressum | Datenschutz</p>
  </aside>

  <div class="hero" role="img" aria-label="Foto: hängender schwarzer Designkamin mit Feuer vor einer Glasfront mit Blick auf eine verschneite Berglandschaft"></div>
  <h1 class="hero-title">WILLKOMMEN IM LINDENHAUS</h1>
  <p class="hero-tagline">KAMINE FÜRS LEBEN</p>
  <p class="hero-cta">Jetzt Beratungstermin vereinbaren</p>
  <svg class="hero-chevron" width="12" height="8" viewBox="0 0 12 8"><path d="M1 1l5 5 5-5" fill="none" stroke="#e4e4e4" stroke-width="1.3"/></svg>

  <section class="hours-popup">
    <h2 class="hours-title">ÖFFNUNGSZEITEN</h2>
    <p class="hours-intro">Wir haben für Sie geöffnet:</p>
    <p class="hours-list"><span>Fr&nbsp; 17.01</span>14:00 - 17:00 Uhr<br><span>Sa 18.01</span>10:00 - 13:00 Uhr</p>
    <div class="hours-divider"></div>
    <p class="hours-links">Weitere Termine ansehen Indiviudellen<br>Termin vereinbaren</p>
  </section>
  <div class="hours-close">x</div>
</div>
</body>
</html>
```